Mutig durchs Jahr
Wir sind richtig begeistert von dieser Möglichkeit, in kurzer Zeit einen guten Entwurf zu erhalten und auch mitgestalten zu können. Vor allem die Auswahl aus verschiedenen Vorschlägen hat unseren eigenen Blick für das geschärft, was wir wollten. Vielen Dank. Es wird sicher nicht das letzte Mal sein, dass wir diese Möglichkeit nutzen.
Zielgruppe
Zielgruppe sind junge Eltern im Stadtteil Richtsberg in Marburg, einem multikulturellen Stadtteil. Die Stadtteilhebamme begleitet junge Familien am Richtsberg vor und nach der Geburt in den ersten Lebensjahren, die NGK (Nachbarschaftsverein Gemeinsam Kreativ e.V.) ist ein Gemeinwesenprojekt die im Stadtteil Anlaufstelle für Stadtteilbewohner, die Beratungsstellen Talwiesenhaus bestehen aus einer Psychologischen Beratungsstelle mit Erziehungsberatung und einer Schwangerenberatungsstelle (in der Stadt)
Aufgabenstellung
Der Text wird als Datei übermittelt, es soll ein Plakat erstellt werden, das
a) die Kooperation der Beteiligten vermittelt
b) das Angebot nahebringt
c) die Kontaktaufnahme ermöglicht
Das Plakat sollte möglichst auch in verkleinerter Form (Din A5?) gedruckt werden können
Das Logo für die NGK ist als Datei angehängt,
das Logo für die Beratungsstellen ist in drei verschiedenen Dateiformaten angehängt. Hier kann auch der Schriftzug "Solvania" wegfallen und nur das Sternenbogen genutzt werden.

```html
<!DOCTYPE html>
<html lang="de">
<head>
<meta charset="utf-8">
<title>Mutig durchs Jahr – Stadtteilhebamme Richtsberg</title>
<link rel="stylesheet" href="https://fonts.googleapis.com/css2?family=Russo+One&family=Archivo:wght@500&family=Pinyon+Script&family=Cormorant+Garamond:ital,wght@0,500;1,500&family=Didact+Gothic&family=Michroma&display=swap">
<style>
  :root {
    --title-blue: #0d4a9c;
    --script-green: #3f9e34;
    --ink: #111111;
    --quote-ink: #1f1f4f;
    --partner-blue: #1a9ee0;
    --assoc-red: #b31f24;
    --band-lilac: #dccbec;
    --paper: #ffffff;
  }
  * { margin: 0; padding: 0; box-sizing: border-box; }
  html, body { width: 848px; height: 1200px; overflow: hidden; background: var(--paper); }
  .poster { position: relative; width: 848px; height: 1200px; overflow: hidden; background: var(--paper); }
  .poster > * { position: absolute; }

  .backdrop { left: 0; top: 0; width: 848px; height: 780px; }
  .map-band { left: 0; top: 775px; width: 848px; height: 425px; }
  .family-art { left: 0; top: 420px; width: 848px; height: 480px; }

  .title-main {
    left: 30px; top: 28px;
    font-family: "Russo One", sans-serif;
    font-size: 104px; line-height: 1;
    color: var(--title-blue);
    letter-spacing: 2px;
    transform: skewX(-14deg);
    transform-origin: left bottom;
  }
  .title-link {
    left: 432px; top: 60px;
    font-family: "Archivo", sans-serif;
    font-weight: 500;
    font-size: 48px; line-height: 1;
    color: var(--ink);
  }
  .title-script {
    left: 360px; top: 100px;
    font-family: "Pinyon Script", cursive;
    font-size: 180px; line-height: 1;
    color: var(--script-green);
    text-shadow: 10px 10px 8px rgba(0,0,0,0.55);
  }

  .partner { left: 182px; top: 146px; display: flex; flex-direction: column; gap: 6px; }
  .partner-square { width: 70px; height: 70px; background: var(--partner-blue); }
  .partner-name {
    font-family: "Didact Gothic", sans-serif;
    font-size: 18px; color: var(--partner-blue);
  }

  .association { left: 192px; top: 268px; }
  .association-mark { display: flex; align-items: center; gap: 12px; }
  .association-dot { width: 60px; height: 60px; border-radius: 50%; background: var(--assoc-red); }
  .association-name {
    font-family: "Cormorant Garamond", serif;
    font-weight: 500;
    font-size: 44px; line-height: 1; color: var(--assoc-red);
  }
  .association-text {
    margin-top: 26px; margin-left: 6px;
    font-family: "Cormorant Garamond", serif;
    font-weight: 500;
    font-size: 15px; line-height: 1.2;
    color: var(--assoc-red);
    text-transform: uppercase;
  }

  .quote {
    left: 440px; top: 282px; width: 340px;
    text-align: center;
    font-family: "Cormorant Garamond", serif;
    font-style: italic; font-weight: 500;
    font-size: 26px; line-height: 1.08;
    color: var(--quote-ink);
  }
  .quote-author {
    left: 440px; top: 356px; width: 340px;
    text-align: center;
    font-family: "Cormorant Garamond", serif;
    font-style: italic; font-weight: 500;
    font-size: 15px; color: var(--quote-ink);
  }

  .offer {
    left: 0; top: 920px; width: 848px;
    text-align: center;
    font-family: "Didact Gothic", sans-serif;
    font-style: italic;
    font-size: 31px; line-height: 46px;
    color: var(--ink);
  }
  .offer span { display: block; transform: skewX(-10deg); }

  .phone {
    left: 0; top: 1106px; width: 848px;
    text-align: center;
    font-family: "Michroma", sans-serif;
    font-size: 14px; letter-spacing: 5px;
    color: var(--ink);
  }
  .website {
    left: 0; top: 1142px; width: 848px;
    text-align: center;
    font-family: "Michroma", sans-serif;
    font-size: 20px; letter-spacing: 4px;
    color: var(--ink);
  }
</style>
</head>
<body>
<main class="poster">
  <svg class="backdrop" viewBox="0 0 848 780" role="img" aria-label="Farbig gemalter Hintergrund mit pinker Blüte, Türkis- und Grüntönen">
    <defs>
      <radialGradient id="bloom" cx="0.28" cy="0.55" r="0.55">
        <stop offset="0" stop-color="#f06ab8"/>
        <stop offset="0.55" stop-color="#f7b6dc"/>
        <stop offset="1" stop-color="#ffffff" stop-opacity="0"/>
      </radialGradient>
      <radialGradient id="aqua" cx="0.95" cy="0.2" r="0.5">
        <stop offset="0" stop-color="#7fd3e4"/>
        <stop offset="1" stop-color="#ffffff" stop-opacity="0"/>
      </radialGradient>
      <radialGradient id="moss" cx="0.92" cy="0.85" r="0.45">
        <stop offset="0" stop-color="#5ea98c"/>
        <stop offset="1" stop-color="#ffffff" stop-opacity="0"/>
      </radialGradient>
    </defs>
    <rect width="848" height="780" fill="#f4fbfb"/>
    <rect width="848" height="780" fill="url(#aqua)"/>
    <rect width="848" height="780" fill="url(#moss)"/>
    <rect width="848" height="780" fill="url(#bloom)"/>
  </svg>

  <svg class="map-band" viewBox="0 0 848 425" role="img" aria-label="Blasser Stadtplan des Stadtteils Richtsberg">
    <rect width="848" height="425" fill="var(--band-lilac)"/>
  </svg>

  <svg class="family-art" viewBox="0 0 848 480" role="img" aria-label="Scherenschnitt-Familie mit Vater, Tochter, Mutter, Sohn und Kinderwagen">
    <defs>
      <filter id="soften" x="-30%" y="-30%" width="160%" height="160%">
        <feGaussianBlur stdDeviation="28"/>
      </filter>
    </defs>
    <g filter="url(#soften)" opacity="0.9">
      <ellipse cx="130" cy="250" rx="95" ry="190" fill="#94a0bb"/>
      <ellipse cx="300" cy="300" rx="85" ry="140" fill="#dc96ee"/>
      <ellipse cx="500" cy="250" rx="110" ry="190" fill="#b796e0"/>
      <ellipse cx="620" cy="390" rx="100" ry="80" fill="#f3cd98"/>
      <ellipse cx="740" cy="300" rx="80" ry="150" fill="#b3f2a6"/>
    </g>
  </svg>

  <div class="title-main">MUTIG</div>
  <div class="title-link">durchs</div>
  <div class="title-script">Jahr</div>

  <div class="partner">
    <div class="partner-square"></div>
    <div class="partner-name">Sternenbogen</div>
  </div>

  <div class="association">
    <div class="association-mark">
      <div class="association-dot"></div>
      <div class="association-name">NGK</div>
    </div>
    <p class="association-text">Nachbarschaftsverein<br>Gemeinsam Kreativ e.V.<br>Marburg</p>
  </div>

  <p class="quote">Und jedem Anfang<br>wohnt ein Zauber inne...</p>
  <p class="quote-author">Lena Vogtmann ©</p>

  <p class="offer">
    <span>Ihre Stadtteilhebamme begleitet junge Familien</span>
    <span>am Richtsberg vor und nach der Geburt</span>
    <span>in den ersten Lebensjahren.</span>
  </p>

  <p class="phone">Fon 00001 / 00 000 00</p>
  <p class="website">WWW.NGK-RICHTSBERG.DE</p>
</main>
</body>
</html>
```